Marlow Orthopaedic Center Mailing Postcard

Need to make a marketing post card to send to patients explaining that:
1. We treat joint pain/problems (shoulder, hip, knee, back)
2. Board Certified and Fellowship Trained Orthopaedic Surgeon (Dr. Gavin Pruitt MD, FAAOS)
3. We are in Harrowgate Trust Building on Fenwick and Ardley
4. Can make an appointment online at www.marlowortho.example
5. Office phone is 847-555-0174
6. Can pull info from www.marlowortho.example
7. Need to put in National Mail Carrier RBMX indicia/stamp on the back of post card (attached below).
8. Would be great if a QR code could be placed on it as well.
9. Logo somewhere on the card.
10. Maybe background map of where the practice is located?? (just an idea)
11. Practice mailing address on the card as well. See website for address.

Obviously a double sided post card to mail. Size should be 6.5 inches by 9 inches.

```html
<!DOCTYPE html>
<html lang="en">
<head>
<meta charset="utf-8">
<title>Marlow Orthopaedic Center Mailing Postcard</title>
<link rel="stylesheet" href="https://fonts.googleapis.com/css2?family=Tinos:wght@400;700&family=Roboto+Condensed:wght@400&display=swap">
<style>
  :root {
    --navy: #14144a;
    --slate: #4b4b47;
    --white: #ffffff;
    --ink: #161616;
    --stage: #dcdcdc;
    --photo-light: #e4e4e6;
    --photo-mid: #b9b7b4;
    --portrait: #8a8f9c;
    --serif: "Tinos", "Times New Roman", serif;
    --sans: "Roboto Condensed", Arial, sans-serif;
  }
  * { margin: 0; padding: 0; box-sizing: border-box; }
  html, body { width: 1014px; height: 1200px; overflow: hidden; }
  body { background: var(--stage); position: relative; font-family: var(--serif); color: var(--ink); }

  .postcard {
    position: absolute; left: 149px; width: 716px; height: 517px;
    background: var(--white); overflow: hidden;
  }
  .postcard--front { top: 67px; }
  .postcard--back { top: 614px; }
  .postcard__shapes { position: absolute; inset: 0; width: 716px; height: 517px; }
  .postcard__text { position: absolute; white-space: nowrap; }

  .brand { color: var(--white); display: flex; align-items: center; gap: 10px; }
  .brand__dot { width: 26px; height: 26px; border-radius: 50%; background: var(--white); flex: none; }
  .brand__name { font-size: 17px; line-height: 1.2; letter-spacing: 0.5px; text-transform: uppercase; }

  .headline { color: var(--white); font-weight: 700; text-transform: uppercase; line-height: 1.15; }
  .front .headline, .postcard--front .headline { font-size: 31px; }
  .joints { color: var(--white); }

  .location { font-size: 17px; line-height: 25px; }
  .contact { font-size: 17px; }
  .contact__sep { margin: 0 6px; }
  .booking { font-size: 12px; }
  .booking b, .booking strong { font-weight: 700; }

  .surgeon { color: var(--white); font-size: 14px; line-height: 20px; }
  .surgeon--right { text-align: right; }

  .mail-to { font-family: var(--sans); font-size: 10px; line-height: 12px; }
  .indicia {
    position: absolute; left: 608px; top: 37px; width: 81px; height: 80px;
    border: 1.5px solid var(--ink); font-family: var(--sans); font-size: 10px; line-height: 12px;
    text-align: center; padding-top: 6px;
  }
  .address-line { position: absolute; left: 370px; width: 319px; height: 0; border-top: 1.5px solid var(--ink); }
</style>
</head>
<body>

<!-- Front side -->
<section class="postcard postcard--front">
  <svg class="postcard__shapes" viewBox="0 0 716 517" aria-hidden="false">
    <defs>
      <linearGradient id="photoTone" x1="0" y1="0" x2="1" y2="1">
        <stop offset="0" stop-color="#eeeeef"/>
        <stop offset="1" stop-color="#b4b0aa"/>
      </linearGradient>
    </defs>
    <circle cx="630" cy="150" r="250" fill="url(#photoTone)" role="img" aria-label="Photo of a clinician guiding a patient walking with a walker in a therapy room"/>
    <circle cx="720" cy="570" r="295" fill="var(--slate)"/>
    <circle cx="200" cy="156" r="207" fill="none" stroke="var(--navy)" stroke-width="2"/>
    <circle cx="200" cy="156" r="200" fill="var(--white)"/>
    <circle cx="200" cy="156" r="193" fill="var(--navy)"/>
    <circle cx="485" cy="287" r="82" fill="var(--navy)"/>
    <circle cx="485" cy="287" r="79" fill="var(--white)"/>
    <circle cx="485" cy="287" r="76" fill="var(--portrait)" role="img" aria-label="Portrait of the orthopaedic surgeon"/>
  </svg>

  <div class="postcard__text brand" style="left:41px; top:44px;">
    <span class="brand__dot"></span>
    <span class="brand__name">Marlow Orthopaedic<br>Center Ltd</span>
  </div>

  <h1 class="postcard__text headline" style="left:39px; top:180px; font-size:31px;">We Treat Joint<br>Pain/Problems</h1>
  <p class="postcard__text joints" style="left:39px; top:263px; font-size:17px;">(Shoulder, Hip, Knee, Back)</p>

  <p class="postcard__text location" style="left:39px; top:385px;">We are in Harrowgate Trust Building<br>on Fenwick and Ardley</p>
  <p class="postcard__text contact" style="left:39px; top:451px;">847-555-0174<span class="contact__sep">|</span>www.marlowortho.example</p>
  <p class="postcard__text booking" style="left:39px; top:477px;">Can make an appointment online at <b>www.marlowortho.example</b></p>

  <p class="postcard__text surgeon surgeon--right" style="right:36px; top:388px;">Board Certified and Fellowship<br><b>Trained Orthopaedic Surgeon</b><br>(Dr. Gavin Pruitt MD, FAAOS)</p>
</section>

<!-- Back side -->
<section class="postcard postcard--back">
  <svg class="postcard__shapes" viewBox="0 0 716 517" aria-hidden="true">
    <circle cx="112" cy="446" r="234" fill="var(--slate)"/>
    <circle cx="127" cy="100" r="208" fill="none" stroke="var(--navy)" stroke-width="2"/>
    <circle cx="127" cy="100" r="201" fill="var(--white)"/>
    <circle cx="127" cy="100" r="194" fill="var(--navy)"/>
  </svg>

  <h2 class="postcard__text headline" style="left:39px; top:66px; font-size:25px;">We Treat Joint<br>Pain/Problems</h2>
  <p class="postcard__text joints" style="left:39px; top:120px; font-size:15px;">(Shoulder, Hip, Knee, Back)</p>
  <p class="postcard__text surgeon" style="left:39px; top:162px; font-size:13.5px;">Board Certified and Fellowship<br>Trained Orthopaedic Surgeon<br>(Dr. Gavin Pruitt MD, FAAOS)</p>

  <div class="postcard__text brand" style="left:41px; top:350px;">
    <span class="brand__dot"></span>
    <span class="brand__name" style="font-size:15px;">Marlow Orthopaedic<br>Center Ltd</span>
  </div>

  <p class="postcard__text surgeon" style="left:39px; top:425px; font-size:15px; line-height:21px;">847-555-0174<br>www.marlowortho.example</p>
  <p class="postcard__text surgeon" style="left:39px; top:470px; font-size:10px;">Can make an appointment online at <b>www.marlowortho.example</b></p>

  <p class="postcard__text mail-to" style="left:370px; top:64px;">Local Postal<br>Customer</p>
  <div class="indicia">Prsrt Std<br>Ecrwss<br>U.S. Postage<br>Paid<br>RBMX retail</div>

  <span class="address-line" style="top:285px;"></span>
  <span class="address-line" style="top:325px;"></span>
  <span class="address-line" style="top:366px;"></span>
</section>

</body>
</html>
```